Rocket business card

Modern business card design, use of color is good with clean space too.

Things to include on card:

Quote: I add fuel to your optometry practice

- Eyewear Sales
- Admin Duties
- Revenue Collection
- Leadership
- Tech Adoption
- COGS Reduction
- Product Sourcing
-Medical Growth

Dalton Vessey, CEO
Glint Harbor
Text Me! 847-302-1964
dalton@glintharbor.example

```html
<!DOCTYPE html>
<html lang="en">
<head>
<meta charset="utf-8">
<title>Glint Harbor Business Card</title>
<link href="https://fonts.googleapis.com/css2?family=Montserrat:wght@400;500;700&display=swap" rel="stylesheet">
<style>
  :root {
    --bg: #2a2a2c;
    --red: #dc3a2c;
    --orange: #e8721f;
    --amber: #f5a11d;
    --ink: #1d1d1f;
    --paper: #ffffff;
  }
  * { box-sizing: border-box; margin: 0; padding: 0; }
  html, body { width: 1200px; height: 900px; overflow: hidden; }
  body {
    background: var(--bg);
    font-family: "Montserrat", sans-serif;
    position: relative;
  }
  .card {
    position: absolute;
    left: 250px;
    width: 700px;
    height: 400px;
    border-radius: 22px;
    overflow: hidden;
  }
  /* Front */
  .card-front {
    top: 30px;
    background: linear-gradient(90deg, var(--red) 0%, var(--orange) 50%, var(--amber) 100%);
    color: var(--paper);
  }
  .brand {
    position: absolute;
    display: flex;
    flex-direction: column;
    align-items: center;
    gap: 18px;
  }
  .card-front .brand { left: 60px; top: 110px; width: 300px; }
  .brand-dot {
    width: 90px; height: 90px; border-radius: 50%;
  }
  .card-front .brand-dot { border: 8px solid var(--paper); }
  .brand-name {
    font-size: 38px;
    font-weight: 500;
    letter-spacing: 2px;
    text-transform: uppercase;
    white-space: nowrap;
  }
  .services {
    position: absolute;
    left: 430px;
    top: 80px;
    list-style: none;
  }
  .services li {
    display: flex;
    align-items: center;
    gap: 10px;
    font-size: 20px;
    font-weight: 500;
    letter-spacing: 1.5px;
    line-height: 30px;
    white-space: nowrap;
  }
  .services svg { width: 16px; height: 16px; flex: none; }

  /* Back */
  .card-back {
    top: 470px;
    background: var(--paper);
    color: var(--ink);
  }
  .card-back .brand { left: 20px; top: 80px; width: 290px; }
  .card-back .brand-dot { background: linear-gradient(90deg, var(--red), var(--amber)); }
  .card-back .brand-name { color: var(--ink); font-size: 30px; }
  .divider {
    position: absolute;
    left: 330px; top: 70px;
    width: 3px; height: 170px;
    background: var(--amber);
  }
  .contact {
    position: absolute;
    left: 355px; top: 72px;
    white-space: nowrap;
  }
  .person-name {
    color: var(--amber);
    font-size: 28px;
    font-weight: 700;
    letter-spacing: 2px;
    text-transform: uppercase;
    line-height: 36px;
  }
  .person-role {
    font-size: 18px;
    letter-spacing: 1px;
    margin-bottom: 16px;
  }
  .contact-line {
    display: flex;
    align-items: center;
    gap: 10px;
    font-size: 16px;
    letter-spacing: 0.5px;
    line-height: 30px;
  }
  .contact-line svg { width: 14px; height: 14px; flex: none; }
  .accent { color: var(--amber); }
  .wave {
    position: absolute;
    left: 0; bottom: 0;
    width: 700px; height: 160px;
  }
</style>
</head>
<body>
  <section class="card card-front">
    <div class="brand">
      <div class="brand-dot"></div>
      <div class="brand-name">Glint Harbor</div>
    </div>
    <ul class="services">
      <li><svg viewBox="0 0 16 16"><path d="M3 3l5 5-5 5M8 3l5 5-5 5" fill="none" stroke="#fff" stroke-width="2"/></svg>Eyewear Sales</li>
      <li><svg viewBox="0 0 16 16"><path d="M3 3l5 5-5 5M8 3l5 5-5 5" fill="none" stroke="#fff" stroke-width="2"/></svg>Admin Duties</li>
      <li><svg viewBox="0 0 16 16"><path d="M3 3l5 5-5 5M8 3l5 5-5 5" fill="none" stroke="#fff" stroke-width="2"/></svg>Revenue Collection</li>
      <li><svg viewBox="0 0 16 16"><path d="M3 3l5 5-5 5M8 3l5 5-5 5" fill="none" stroke="#fff" stroke-width="2"/></svg>Leadership</li>
      <li><svg viewBox="0 0 16 16"><path d="M3 3l5 5-5 5M8 3l5 5-5 5" fill="none" stroke="#fff" stroke-width="2"/></svg>Tech Adoption</li>
      <li><svg viewBox="0 0 16 16"><path d="M3 3l5 5-5 5M8 3l5 5-5 5" fill="none" stroke="#fff" stroke-width="2"/></svg>COGS Reduction</li>
      <li><svg viewBox="0 0 16 16"><path d="M3 3l5 5-5 5M8 3l5 5-5 5" fill="none" stroke="#fff" stroke-width="2"/></svg>Product Sourcing</li>
      <li><svg viewBox="0 0 16 16"><path d="M3 3l5 5-5 5M8 3l5 5-5 5" fill="none" stroke="#fff" stroke-width="2"/></svg>Medical Growth</li>
    </ul>
  </section>

  <section class="card card-back">
    <div class="brand">
      <div class="brand-dot"></div>
      <div class="brand-name">Glint Harbor</div>
    </div>
    <div class="divider"></div>
    <div class="contact">
      <div class="person-name">Dalton Vessey</div>
      <div class="person-role">CEO</div>
      <div class="contact-line">
        <svg viewBox="0 0 16 16"><path d="M4 1l3 3-2 2c1 2 3 4 5 5l2-2 3 3-2 3C7 15 1 9 1 3z" fill="#f5a11d"/></svg>
        847-302-1964
      </div>
      <div class="contact-line">
        <svg viewBox="0 0 16 16"><rect x="1" y="3" width="14" height="10" fill="none" stroke="#f5a11d" stroke-width="1.6"/><path d="M1 3l7 6 7-6" fill="none" stroke="#f5a11d" stroke-width="1.6"/></svg>
        dalton@glintharbor.example
      </div>
      <div class="contact-line">
        <svg viewBox="0 0 16 16"><circle cx="8" cy="8" r="6.5" fill="none" stroke="#f5a11d" stroke-width="1.4"/><path d="M1.5 8h13M8 1.5c-3 3-3 10 0 13M8 1.5c3 3 3 10 0 13" fill="none" stroke="#f5a11d" stroke-width="1.2"/></svg>
        <span>www.<span class="accent">glintharbor</span>.example</span>
      </div>
    </div>
    <svg class="wave" viewBox="0 0 700 160" preserveAspectRatio="none" aria-hidden="true">
      <defs>
        <linearGradient id="waveGrad" x1="0" x2="1" y1="0" y2="0">
          <stop offset="0" stop-color="#dc3a2c"/>
          <stop offset="0.5" stop-color="#e8721f"/>
          <stop offset="1" stop-color="#f5a11d"/>
        </linearGradient>
      </defs>
      <path d="M0 40 C120 80 260 110 420 110 L0 110 Z" fill="url(#waveGrad)"/>
      <path d="M0 60 C140 110 300 120 420 110 C540 100 640 120 700 160 L0 160 Z" fill="#1d1d1f"/>
      <path d="M0 70 C150 120 320 125 430 118 C560 108 650 130 700 160 L0 160 Z" fill="#ffffff"/>
      <path d="M150 160 C300 110 470 110 560 125 C620 135 670 150 700 160 Z" fill="url(#waveGrad)"/>
    </svg>
  </section>
</body>
</html>
```